Mortgage Loan officer needs clean/modern business card design

Looking for a clean, modern 2-sided business card design. We like the earth tones used in our logo and website http://vukarhome-lending.example . Would also like to incorporate: 1) Something special to make our card stand out - a pop of color or embossed logo, for instance and 2) please include "Mortgage Loans" "Reverse Mortgages" "Private Money Loans" on back of card with the logo.

Front: Needs to include agent/company license info - see website. Agent name: Niall Hargrove

Here are fonts and colors used for our logo:
Font: Avenir Next
Colors:
#2c3539 - Dark Gray
#576870 - Light Gray
#ffffff - Background White

Target Market(s)

Prospects and current clients. Will also be distributing to people in professional network (attorneys and CPAs)

Industry/Entity Type

Business

Contact Information for Business Card

Include agent name, contact info, website on front, licensing info for agent an company. Logo and services offered on back

Font styles to use
Other font styles liked:
• Avenir Next

Requirements
Must have
• See project description
Should not have
• Nothing cheesy

```html
<!DOCTYPE html>
<html lang="en">
<head>
<meta charset="utf-8">
<title>Vukar Home Lending – Business Card</title>
<link rel="stylesheet" href="https://fonts.googleapis.com/css2?family=Nunito+Sans:wght@400;600;700&display=swap">
<style>
  :root {
    --dark-gray: #2c3539;
    --light-gray: #576870;
    --white: #ffffff;
    --stage: #000000;
    --ring: #2f3a3e;
  }
  * { margin: 0; padding: 0; box-sizing: border-box; }
  html, body {
    width: 1200px; height: 900px; overflow: hidden;
    background: var(--stage);
    font-family: "Nunito Sans", "Avenir Next", Arial, sans-serif;
  }
  .stage { position: relative; width: 1200px; height: 900px; }

  .card {
    position: absolute;
    width: 477px;
    overflow: hidden;
    background: var(--dark-gray);
  }
  .card--front { left: 116px; top: 275px; height: 293px; border-radius: 0 46px 0 46px; }
  .card--back  { left: 622px; top: 276px; height: 292px; border-radius: 46px 0 46px 0; }

  .band { position: absolute; left: 0; width: 100%; }
  .band--top { top: 0; background: var(--light-gray); }
  .band--middle { background: var(--white); }
  .card--front .band--top { height: 92px; }
  .card--front .band--middle { top: 92px; height: 99px; }
  .card--back .band--top { height: 97px; }
  .card--back .band--middle { top: 97px; height: 98px; }

  .emblem {
    position: absolute;
    width: 154px; height: 154px;
    border-radius: 50%;
    background: var(--white);
    border: 8px solid var(--ring);
    display: flex; align-items: center; justify-content: center;
    text-align: center;
  }
  .card--front .emblem { left: 162px; top: 65px; }
  .card--back .emblem { left: 161px; top: 70px; }
  .emblem__name {
    color: var(--light-gray);
    font-size: 19px; font-weight: 600; line-height: 1.2;
  }

  .agent {
    position: absolute; top: 24px; left: 0; width: 100%;
    text-align: center; color: var(--white);
    white-space: nowrap;
  }
  .agent__name { font-size: 16px; font-weight: 700; letter-spacing: .2px; }
  .agent__divider { font-size: 17px; margin: 0 6px; }
  .agent__title { font-size: 13px; font-weight: 400; }

  .contact {
    position: absolute; top: 217px; left: 0; width: 100%;
    text-align: center; color: var(--white);
    font-size: 13px; line-height: 16px;
  }
  .contact__address { margin-top: 10px; }

  .services {
    position: absolute; top: 234px; left: 0; width: 100%;
    text-align: center; color: var(--white);
    font-size: 13px; font-weight: 700; line-height: 17px;
  }
</style>
</head>
<body>
<main class="stage">
  <section class="card card--front" aria-label="Card front">
    <div class="band band--top"></div>
    <div class="band band--middle"></div>
    <p class="agent">
      <span class="agent__name">NIALL HARGROVE</span><span class="agent__divider">|</span><span class="agent__title">Managing Director</span>
    </p>
    <div class="emblem"><span class="emblem__name">Vukar Home<br>Lending</span></div>
    <div class="contact">
      <p>041-555-0182 &nbsp;|&nbsp; 041-555-0149</p>
      <p>info@vukarhome-lending.example &nbsp;|&nbsp; www.vukarhome-lending.example</p>
      <p class="contact__address">1234 Address Tag Line | Country Name, AB | 123456</p>
    </div>
  </section>

  <section class="card card--back" aria-label="Card back">
    <div class="band band--top"></div>
    <div class="band band--middle"></div>
    <div class="emblem"><span class="emblem__name">Vukar Home<br>Lending</span></div>
    <div class="services">
      <p>Mortgage Loans &nbsp;|&nbsp; Reverse Mortgages</p>
      <p>Private Money Loans</p>
    </div>
  </section>
</main>
</body>
</html>
```